Stationary and Business Card for eDiscovery Tech Company
Varendra Systems
Stationary and Business Card for eDiscovery Tech Company - Software
Creative Brief
Professional
Marcus T. Hellerby
Chief Executive Officer
48712 Larkspur Mill Rd Suite K340 - 500 Katy, TX 77494
tkolvern@varendra.example
www.varendra.example
In general: Our company is currently focused on providing software solutions to the legal industry for electronic discovery. While our company is forward thinking in its technology we still embrace conservative business standards, professionalism is key. For the business card: We want a clean design that is not cluttered. Omitting the mailing address would be acceptable. We have both stacked and side by side layouts of our logo, feel free to use either and be creative. We are considering the inclusion of a QR code, possibly on the back of the card unless it can be done well in the front design. IF it needs to be done on the back we would like to include a line of explanation such as "Contact information provided in QR code format for your convenience". The initial perception by the recipient of the card is important to us. We are considering moderate weight, linen textured cards (any insight as to complications with a linen texture card from a design perspective, please let me know) We are also considering the use of a card with rounded edges (In the event this should be taken into consideration for your design options) For the letterhead/stationary and envelope: We will need Microsoft Word template/document of the winning design for these items as well. Please do not hesitate to ask any questions. I look forward to working with you.
Possibly a QR code containing contact information.
tkolvern tkolvern
Cards which are heavily bisected with a large logo on one side and lots of stacks stacked on the opposite side seem cluttered and not something desired for this project. Additionally, I am finding designs which are using a colored background where the majority of the text is in white are more difficult to read.
I have come to realize my request to include a line of text with the QR code was a really bad idea. Please disregard using any decriptive text about including contact information by the qr code.

```html
<!DOCTYPE html>
<html lang="en">
<head>
<meta charset="utf-8">
<title>Varendra Systems — Business Card</title>
<link href="https://fonts.googleapis.com/css2?family=Exo+2:wght@400;600;700&family=Open+Sans:wght@400;600;700&display=swap" rel="stylesheet">
<style>
  :root{
    --bg:#2b2d31;
    --card:#ffffff;
    --ink:#2a2d33;
    --muted:#6b7079;
    --navy:#0f2f57;
    --blue:#1c74c4;
    --sky:#3fa3e8;
    --chip:#c9ced6;
    --chip-dark:#8e96a3;
  }
  *{box-sizing:border-box;margin:0;padding:0}
  html,body{width:1200px;height:1077px;overflow:hidden}
  body{background:var(--bg);position:relative;font-family:"Open Sans",sans-serif;color:var(--ink)}

  .card{position:absolute;left:260px;width:680px;height:389px;background:var(--card);
        box-shadow:0 14px 40px rgba(0,0,0,.45);overflow:hidden}
  .card--front{top:90px}
  .card--back{top:598px}

  /* front */
  .band{position:absolute;left:318px;top:0;width:52px;height:100%;
        background:linear-gradient(180deg,var(--sky) 0%,var(--blue) 45%,var(--navy) 100%)}
  .band-chips{position:absolute;left:0;top:0;width:100%;display:flex;flex-direction:column}
  .band-chips span{display:block;height:34px}
  .band-chips span:nth-child(1){background:var(--chip-dark)}
  .band-chips span:nth-child(2){background:var(--chip)}
  .band-chips span:nth-child(3){background:#eef1f5}

  .contact{position:absolute;left:150px;top:40px;text-align:right;width:140px}
  .contact h3{font-family:"Exo 2",sans-serif;font-weight:700;font-size:15px;letter-spacing:.5px;color:var(--ink);margin-bottom:6px}
  .contact p{font-size:10.5px;line-height:1.45;color:var(--muted);white-space:nowrap}

  .brand{display:flex;align-items:center;gap:12px}
  .brand-dot{width:44px;height:44px;border-radius:50%;background:var(--blue);flex:none}
  .brand-name{font-family:"Exo 2",sans-serif;font-weight:700;color:var(--navy);line-height:1}
  .brand-name span{display:block}
  .card--front .brand{position:absolute;left:88px;top:178px}
  .card--front .brand-name{font-size:28px}

  .social{position:absolute;left:410px;top:40px}
  .social h3{font-family:"Exo 2",sans-serif;font-weight:700;font-size:14px;color:var(--ink);margin-bottom:6px}
  .social p{font-size:10.5px;line-height:1.45;color:var(--muted)}

  .person{position:absolute;left:410px;top:270px}
  .person-name{font-family:"Exo 2",sans-serif;font-weight:700;font-size:18px;letter-spacing:.5px;color:var(--ink)}
  .person-role{font-size:11px;font-weight:600;letter-spacing:1px;color:var(--muted);margin-top:4px}

  /* back */
  .card--back .brand{position:absolute;left:50%;top:50%;transform:translate(-50%,-50%);gap:18px}
  .card--back .brand-dot{width:70px;height:70px}
  .card--back .brand-name{font-size:44px}
</style>
</head>
<body>
  <section class="card card--front" aria-label="Business card front">
    <div class="contact">
      <h3>CONTACT US</h3>
      <p>555 014 2290</p>
      <p>tkolvern@varendra.example</p>
      <p>www.varendra.example</p>
    </div>
    <div class="brand">
      <span class="brand-dot"></span>
      <span class="brand-name"><span>Varendra</span><span>Systems</span></span>
    </div>
    <div class="band">
      <div class="band-chips"><span></span><span></span><span></span></div>
    </div>
    <div class="social">
      <h3>FOLLOW US ON SOCIAL</h3>
      <p>linkhub.example/user-name</p>
      <p>chirpline.example/user-name</p>
      <p>folioboard.example/user-name</p>
    </div>
    <div class="person">
      <div class="person-name">OWEN HARTLEY</div>
      <div class="person-role">FOUNDER</div>
    </div>
  </section>

  <section class="card card--back" aria-label="Business card back">
    <div class="brand">
      <span class="brand-dot"></span>
      <span class="brand-name"><span>Varendra</span><span>Systems</span></span>
    </div>
  </section>
</body>
</html>
```